Web Design Project

The aim of this project to design a website for a service that would offer services for small business and non profit organizations using opensource software that is weaved to work together in harmony.

The website name is: velisto.net

Tavrel in Arabic means: cabbage. Cabbage is composed of leaves, actually there is nothing except leaves. Each leave by itself is not called cabbage, but a collection of leaves that are organized in a central way would give us cabbage.

Same idea for Tavrel where open source software very well organized and integrated would create a new thing with a new value.
Updates

Target Market(s)

Small business, Europe, Africa, Far east and Middle east

Industry/Entity Type

Small Business

Requirements
Must have
• The website would offer the following sections:
* Home page
* Benefits: value of tavrel
* Applications: applications offered by tavrel
* Pricing
* Purchase
* Customer log in
* Support
- FAQ
- Knowledge base
- Forums
- Open tickets

Please take the following consideration in design:
* White should predominate
* Only black and the colors of logo are permitted (attched)
Nice to have
• Design is better to express:
* Openness
* Dynamic
* Usable
* Cost effective

```html
<!DOCTYPE html>
<html lang="en">
<head>
<meta charset="utf-8">
<title>Tavrel — start small and grow</title>
<link href="https://fonts.googleapis.com/css2?family=Arimo:wght@400;700&family=Questrial&family=Tinos:ital@1&display=swap" rel="stylesheet">
<style>
:root{
  --yellow:#f5bd00;
  --green:#80bc24;
  --blue:#0b8fd6;
  --magenta:#b84f95;
  --ink:#111;
  --text:#333;
  --muted:#666;
  --line:#dcdcdc;
  --panel:#f2f2f2;
  --header:#f7f7f7;
}
*{box-sizing:border-box;margin:0;padding:0}
html,body{width:1200px;height:1130px;overflow:hidden}
body{font-family:"Arimo",Arial,sans-serif;color:var(--text);background:#fff;position:relative;border-top:4px solid var(--ink);border-bottom:5px solid var(--ink)}
a{text-decoration:none;color:inherit}

/* header */
.site-header{position:absolute;top:0;left:0;width:1200px;height:124px;background:linear-gradient(#fff,var(--header));border-bottom:1px solid #e3e3e3}
.brand{position:absolute;left:222px;top:48px;display:flex;align-items:center;gap:10px;font-family:"Questrial",sans-serif;font-size:36px;color:var(--ink)}
.brand-dot{width:22px;height:22px;border-radius:50%;background:var(--green)}
.tagline{position:absolute;left:480px;top:36px;width:390px;text-align:right;font-family:"Tinos",serif;font-style:italic;font-size:10.5px;color:#888}
.login-pill{position:absolute;left:876px;top:28px;height:28px;padding:0 6px 0 10px;border:1px solid #d6d6d6;border-radius:14px;background:#fff;display:flex;align-items:center;gap:5px;font-size:10px;font-weight:700;color:#555}
.login-pill .arrow{width:20px;height:20px;border-radius:50%;background:var(--blue);display:flex;align-items:center;justify-content:center}
.main-nav{position:absolute;left:485px;top:78px;height:46px;display:flex;border-left:1px solid #e0e0e0}
.main-nav a{display:flex;align-items:center;padding:0 9px;border-right:1px solid #e0e0e0;font-weight:700;font-size:12.5px}
.main-nav .home{padding:0 14px}
.c-y{color:var(--yellow)}.c-g{color:var(--green)}.c-b{color:var(--blue)}.c-m{color:var(--magenta)}

/* hero */
.hero{position:absolute;top:124px;left:0;width:1200px;height:349px;background:linear-gradient(#f0ede6 0%,#f1e4cf 40%,#e8d4bb 55%,#a9b5bd 63%,#8ea3b0 80%,#a5b5c0 100%)}
.hero h1{position:absolute;top:57px;width:1200px;text-align:center;font-family:"Questrial",sans-serif;font-weight:400;font-size:38px;color:var(--ink)}
.search{position:absolute;left:340px;top:122px;width:519px;height:39px;display:flex;border:1px solid #cfcfcf;border-radius:3px;background:#fff}
.search-field{flex:1}
.search-btn{width:92px;border-left:1px solid #d6d6d6;background:linear-gradient(#fafafa,#ececec);display:flex;align-items:center;justify-content:center;gap:6px;font-family:"Questrial",sans-serif;font-size:14px;color:var(--blue)}
.hero-note{position:absolute;top:168px;width:1200px;text-align:center;font-size:10.5px;color:var(--ink)}
.hero-note a{color:var(--blue)}

/* cards */
.cards{position:absolute;left:200px;top:438px;display:flex;gap:7px}
.card{width:195px;height:230px;background:var(--panel);border:1px solid #e0e0e0;border-top:none}
.card h2{height:38px;display:flex;align-items:center;justify-content:center;font-size:12px;font-weight:700;color:#fff}
.card ul{list-style:none;margin:5px 25px 0}
.card li{font-size:11.5px;color:#444;height:27.8px;line-height:27px;border-bottom:1px solid #dedede}
.card li:last-child{border-bottom:none}
.more{display:block;text-align:right;margin:6px 27px 0 0;font-size:10px;font-weight:700}
.more b{font-size:12px;margin-right:4px}
.bg-y{background:var(--yellow)}.bg-g{background:var(--green)}.bg-b{background:var(--blue)}.bg-m{background:var(--magenta)}

/* welcome */
.welcome{position:absolute;left:200px;top:720px;width:498px}
.welcome h2{font-weight:400;font-size:28px;line-height:28px;color:var(--blue)}
.welcome h2 span{color:var(--ink)}
.welcome p{font-size:10.2px;line-height:14.5px;color:var(--ink);margin-top:8px}
.welcome p em{font-style:normal;color:#777}
.welcome hr{border:none;border-top:1px solid var(--line);margin:15px 0 18px}
.about{display:flex;gap:30px}
.about-mark{width:102px;height:74px;flex:none;display:flex;align-items:center;gap:6px;font-family:"Questrial",sans-serif;font-size:22px;color:var(--green)}
.about-mark i{width:16px;height:16px;border-radius:50%;background:var(--magenta)}
.about p{margin-top:0}
.divider{position:absolute;left:714px;top:718px;height:230px;border-left:1px solid var(--line)}

/* sidebar */
.sidebar{position:absolute;left:741px;top:716px;width:259px}
.sidebar h3{font-weight:400;font-size:13.5px;color:var(--ink)}
.sidebar p{font-size:7.8px;line-height:11.3px;color:#555;margin-top:6px}
.btn-member{display:inline-flex;align-items:center;gap:14px;margin-top:8px;height:28px;padding:0 16px;border-radius:14px;background:var(--ink);color:#fff;font-size:10px;font-weight:700}
.mobile{margin-top:38px}
.stores{display:flex;gap:10px;margin-top:8px}
.store{width:124px;height:39px;border-radius:5px;background:#1a1a1a;border:1px solid #777}

/* footer */
.site-footer{position:absolute;top:1024px;left:0;width:1200px;height:101px;background:var(--panel);border-top:1px solid #e0e0e0}
.foot-nav{position:absolute;left:200px;top:24px;display:flex;font-size:10.5px;color:#444}
.foot-nav a{padding:0 10px;border-left:1px solid #ccc;line-height:12px}
.foot-nav a:first-child{padding-left:0;border-left:none}
.social{position:absolute;left:914px;top:17px;display:flex;gap:3px}
.social span{width:27px;height:27px}
.foot-rule{position:absolute;left:200px;top:52px;width:800px;border-top:1px solid var(--line)}
.copy{position:absolute;left:199px;top:70px;font-size:10px;color:#444}
.copy b{color:var(--ink)}
</style>
</head>
<body>

<header class="site-header">
  <a class="brand" href="#"><span class="brand-dot"></span>tavrel</a>
  <p class="tagline">Lorem ipsum dolor sit amet, consectetur adipisicing elit, sed do eiusmod tempor</p>
  <a class="login-pill" href="#">Customer Log-in
    <span class="arrow"><svg width="8" height="10" viewBox="0 0 8 10"><path d="M2 1l4 4-4 4" fill="none" stroke="#fff" stroke-width="2"/></svg></span>
  </a>
  <nav class="main-nav">
    <a class="home" href="#"><svg width="16" height="14" viewBox="0 0 16 14"><path d="M8 0L0 7h2v7h4V9h4v5h4V7h2z" fill="var(--yellow)"/></svg></a>
    <a class="c-g" href="#">Benefits</a>
    <a class="c-b" href="#">Applications</a>
    <a class="c-m" href="#">Pricing</a>
    <a class="c-g" href="#">Purchase</a>
    <a class="c-b" href="#">Forum</a>
    <a class="c-m" href="#">Support</a>
    <a class="c-g" href="#">Contact Us</a>
  </nav>
</header>

<section class="hero" role="img" aria-label="Soft-focus photograph of a calm sea at sunrise">
  <h1>start small and grow.</h1>
  <form class="search">
    <div class="search-field"></div>
    <div class="search-btn"><svg width="15" height="15" viewBox="0 0 15 15"><circle cx="6" cy="6" r="4.5" fill="none" stroke="var(--blue)" stroke-width="2"/><path d="M9.5 9.5l4 4" stroke="var(--blue)" stroke-width="2.4" stroke-linecap="round"/></svg>Search</div>
  </form>
  <p class="hero-note">Lorem ipsum dolores? View demo <a href="#">here</a>.</p>
</section>

<section class="cards">
  <article class="card">
    <h2 class="bg-y">Benefits: Value of Tavrel</h2>
    <ul><li>Ongoing Support</li><li>Total Control</li><li>Weaved in Harmony</li><li>Safe and PCI Compliant</li><li>Cost Effective</li></ul>
    <a class="more c-y" href="#"><b>+</b>View More</a>
  </article>
  <article class="card">
    <h2 class="bg-g">Applications and Softwares</h2>
    <ul><li>Business App</li><li>Software Sample</li><li>Placeholder 3</li><li>Tavrel Application 3.0</li><li>Desktop Suite Seven</li></ul>
    <a class="more c-g" href="#"><b>+</b>View More</a>
  </article>
  <article class="card">
    <h2 class="bg-b">Forum: Knowledge Based</h2>
    <ul><li>Community Programs</li><li>Members Forum</li><li>Tavrel Center</li><li>Authors and Contributors</li><li>Live Dolor Sit Amet</li></ul>
    <a class="more c-b" href="#"><b>+</b>View More</a>
  </article>
  <article class="card">
    <h2 class="bg-m">Recent Software Updates</h2>
    <ul><li>Change Logs</li><li>3.1.1 Update Available</li><li>Sit Amet Conspig</li><li>Configurations</li><li>Cross Compatibility</li></ul>
    <a class="more c-m" href="#"><b>+</b>View More</a>
  </article>
</section>

<section class="welcome">
  <h2>Welcome to <span>tavrel,</span><br>duis aute irure dolor in reprehenderit.</h2>
  <p>Hello, we’re Tavrel and lorem ipsum dolor sit amet, <em>simple service</em> elit, sed do eiusmod tempor incididunt ut labore et dolore magna aliqua. Ut enim ad minim veniam, quis nostrud exercitation ullamco laboris nisi ut aliquip <em>small business and non profit organizations</em>. Duis aute irure dolor in <em>opensource software</em> velit.</p>
  <hr>
  <div class="about">
    <div class="about-mark"><i></i>tavrel</div>
    <p>Sed ut perspiciatis unde omnis iste natus error sit voluptatem accusantium doloremque laudantium, totam rem aperiam, eaque ipsa qae ab illo inventore veritatis et quasi architeo beatae vitae dicta sunt expicabo. Nemo enim ipsam voluptatem quia voluptas sit aspernatur aut odit aut fugit, sed qua consequtur magni dolores eos qui ratione voluptatem sequi nesciunt.</p>
  </div>
</section>
<div class="divider"></div>

<aside class="sidebar">
  <h3>Members Section</h3>
  <p>Nam libero tempore, cum soluta nobis est eligendi optio cumque nihil impedit quo minus id quod maxime placeat facere possimus.</p>
  <a class="btn-member" href="#">Member Login <svg width="6" height="9" viewBox="0 0 6 9"><path d="M1 1l3.5 3.5L1 8" fill="none" stroke="#fff" stroke-width="1.6"/></svg></a>
  <div class="mobile">
    <h3>Tavrel On Your Mobile</h3>
    <p>Temporibus autem quibusdam et aut officiis debitis aut rerum necessitatibus saepe eveniet ut et voluptates repudiandae sint et molestiae non recusandae. Itaque earum rerum hic tenetur astr.</p>
    <div class="stores"><span class="store"></span><span class="store"></span></div>
  </div>
</aside>

<footer class="site-footer">
  <nav class="foot-nav">
    <a href="#">Home</a><a href="#">Benefits</a><a href="#">Applications</a><a href="#">Pricing</a><a href="#">Purchase</a><a href="#">Forum</a><a href="#">Support</a><a href="#">Contact Us</a><a href="#">Customer Login</a>
  </nav>
  <div class="social"><span style="background:#5ec3e8"></span><span style="background:#1b7fb3"></span><span style="background:#3e5f9c"></span></div>
  <div class="foot-rule"></div>
  <p class="copy">Copyright 2013 <b>Tavrel</b>. All Rights Reserved.</p>
</footer>

</body>
</html>
```